Business Card Design Project (Beer industry)

I am seeking a redesign of my business card. I am looking for something that will really stand out in both texture and feel. Something more on the modern side then traditional. Nothing die cut shaped like a beer mug please.

The card is used mostly for other industry professionals, as well as bar and restaurant owners. My title is Strategy & Acquisitions. If you would like to somehow incorporate that theme, that may work.

My business is craft and imported beer. Nothing fizzy and yellow, so my products are more on the upscale side.
Updates

I was able to update my logo in .ai and .tif format. I hope that helps. 

Thank you all for your creative ideas. I have uploaded my current business card in pdf format, as well as our logo in .eps file format. We are excited about the submissions so far and want to thank you all again.

PS Please do not include fax number in future submissions, as we are looking for something more creative and a fax says 1999 and not 2015, which is the message we are going for, without being futuristic. 

Thank you all once again for all of your submissions. If we would consider a two sided card, we would like the opposite side not to be the same as the front. The styles we have seen so far, it appears the front and back are too similar. Again, a two sided card is not required. Thank you and we look forward to pushing the boundaries of your creativity. Cheers

Target Market(s)

My card would mostly go to bar and restaurant operators as well as other beer industry professionals

Industry/Entity Type

Restaurant

Requirements
Nice to have
• Two sided would be considered, although not required
Should not have
• Anything die cut shaped like a beer mug.

```html
<!DOCTYPE html>
<html lang="en">
<head>
<meta charset="utf-8">
<title>Northgate Ales – Business Card</title>
<link href="https://fonts.googleapis.com/css2?family=EB+Garamond:wght@400&family=Lora:ital,wght@1,400&family=Ubuntu:wght@400;500&display=swap" rel="stylesheet">
<style>
  :root{
    --bg:#4a2c20;
    --card-light:#f59d1e;
    --card-dark:#e8850b;
    --ink-red:#a3331a;
    --ink-blue:#263f68;
    --deco-blue:#3a5d97;
    --deco-blue-dark:#22385f;
  }
  *{margin:0;padding:0;box-sizing:border-box}
  html,body{width:1200px;height:1000px;overflow:hidden;background:var(--bg)}
  .canvas{position:relative;width:1200px;height:1000px}
  .card{
    position:absolute;border-radius:18px;overflow:hidden;
    background:linear-gradient(160deg,var(--card-light),var(--card-dark));
  }
  .card-front{left:43px;top:42px;width:765px;height:435px}
  .card-back{left:383px;top:508px;width:763px;height:436px}

  /* front */
  .brand{position:absolute;left:52px;top:30px;width:360px;height:300px;text-align:center}
  .brand-mark{display:block;margin:50px auto 0;width:96px;height:96px;border-radius:50%;background:var(--ink-blue)}
  .brand-name{
    display:block;margin-top:48px;
    font-family:"Ubuntu",sans-serif;font-weight:500;font-size:36px;letter-spacing:1px;color:var(--ink-red)
  }
  .brand-city{
    position:absolute;left:52px;top:325px;width:360px;text-align:center;
    font-family:"Lora",serif;font-style:italic;font-size:38px;color:var(--ink-blue)
  }
  .brand-tagline{
    position:absolute;left:52px;top:380px;width:360px;text-align:center;
    font-family:"Lora",serif;font-style:italic;font-size:16px;color:#7a2a14
  }
  .person{position:absolute;left:487px;top:182px}
  .person-name{font-family:"EB Garamond",serif;font-weight:400;font-size:36px;color:var(--ink-blue);line-height:1.1}
  .person-title{font-family:"EB Garamond",serif;font-size:20px;color:var(--ink-blue);margin-top:8px;margin-left:6px}

  /* back */
  .contact-list{position:absolute;left:54px;top:41px;list-style:none}
  .contact-item{
    display:flex;align-items:center;height:51px;
    font-family:"Ubuntu",sans-serif;font-size:25px;color:var(--ink-red)
  }
  .contact-item.no-icon{padding-left:47px}
  .contact-icon{width:28px;height:28px;margin-right:19px;flex:none}
  .skyline-art{
    position:absolute;left:410px;right:22px;top:160px;bottom:0;
    background:linear-gradient(180deg,var(--deco-blue) 0%,var(--deco-blue-dark) 100%);
    border-radius:14px 14px 0 0;
  }
</style>
</head>
<body>
<main class="canvas">

  <section class="card card-front">
    <div class="brand">
      <span class="brand-mark"></span>
      <span class="brand-name">NORTHGATE ALES</span>
    </div>
    <p class="brand-city">New York</p>
    <p class="brand-tagline">Premier Craft &amp; Import Beer Distributor</p>
    <div class="person">
      <h1 class="person-name">Dana Holloway</h1>
      <p class="person-title">Strategy &amp; Acquisitions</p>
    </div>
  </section>

  <section class="card card-back">
    <ul class="contact-list">
      <li class="contact-item">
        <svg class="contact-icon" viewBox="0 0 28 28"><rect width="28" height="28" rx="2" fill="var(--ink-red)"/><path d="M14 5a6 6 0 0 0-6 6c0 4.5 6 12 6 12s6-7.5 6-12a6 6 0 0 0-6-6zm0 8.3a2.3 2.3 0 1 1 0-4.6 2.3 2.3 0 0 1 0 4.6z" fill="var(--card-light)"/></svg>
        58 Foundry Street
      </li>
      <li class="contact-item no-icon">Brooklyn, NY 11222</li>
      <li class="contact-item">
        <svg class="contact-icon" viewBox="0 0 28 28"><rect width="28" height="28" rx="2" fill="var(--ink-red)"/><path d="M5 11c0-3 4-4 9-4s9 1 9 4v2h-4v-2h-10v2H5z" fill="var(--card-light)"/><rect x="7" y="14" width="14" height="8" rx="1" fill="var(--card-light)"/><circle cx="14" cy="18" r="2" fill="var(--ink-red)"/></svg>
        (718) 555-0142
      </li>
      <li class="contact-item">
        <svg class="contact-icon" viewBox="0 0 28 28"><rect width="28" height="28" rx="2" fill="var(--ink-red)"/><rect x="8" y="4" width="12" height="20" rx="2" fill="var(--card-light)"/><rect x="10" y="7" width="8" height="12" fill="var(--ink-red)"/><circle cx="14" cy="21.5" r="1" fill="var(--ink-red)"/></svg>
        (917) 555-0187
      </li>
      <li class="contact-item">
        <svg class="contact-icon" viewBox="0 0 28 28"><rect width="28" height="28" rx="2" fill="var(--ink-red)"/><rect x="5" y="8" width="18" height="12" fill="var(--card-light)"/><path d="M5 8l9 7 9-7" fill="none" stroke="var(--ink-red)" stroke-width="1.6"/></svg>
        dana@ngales.com
      </li>
      <li class="contact-item">
        <svg class="contact-icon" viewBox="0 0 28 28"><rect width="28" height="28" rx="2" fill="var(--ink-red)"/><g fill="none" stroke="var(--card-light)" stroke-width="1.6"><circle cx="14" cy="14" r="8"/><ellipse cx="14" cy="14" rx="3.5" ry="8"/><path d="M6 14h16M7.5 10h13M7.5 18h13"/></g></svg>
        www.northgateales.com
      </li>
    </ul>
    <div class="skyline-art" role="img" aria-label="Illustrated New York skyline with a statue silhouette and three stars in blue"></div>
  </section>

</main>
</body>
</html>
```